Swimming Pool Business Billboard

10' x 24' Billboard displaying company name, logo and phone number. Picture of swimming pool activity; kids playing , swimming, etc. Bullet points possibly shown: New Construction, Repairs, Weekly maintenance.

Industry/Entity Type

Swimming pool construction, repairs and maintenance.

Font styles to use
Sans Serif

Colors
0054AA
0677BA
7BADD7
CADEEF
E8F1F8

Requirements
Must have
• Rusty & Calder Pembrook, RUSTY'S POOLS & Service,
Nice to have
• Prefer to have my last name "Pembrook" above the word "POOLS" only in smaller print so that "RUSTYS POOLS" is distinguished.

```html
<!DOCTYPE html>
<html lang="en">
<head>
<meta charset="UTF-8">
<title>Rusty's Pools Billboard</title>
<link href="https://fonts.googleapis.com/css2?family=Poppins:wght@500;600;700&display=swap" rel="stylesheet">
<style>
  :root {
    --brand-blue: #0054AA;
    --ocean-blue: #0677BA;
    --sky-blue: #7BADD7;
    --mist-blue: #CADEEF;
    --foam-blue: #E8F1F8;
    --navy: #0B3F74;
    --white: #FFFFFF;
    --page: #F4F6F8;
  }
  html, body {
    margin: 0;
    padding: 0;
    width: 1130px;
    height: 1200px;
    overflow: hidden;
    background: var(--page);
    font-family: "Poppins", sans-serif;
  }
  .canvas {
    position: relative;
    width: 1130px;
    height: 1200px;
  }
  .billboard {
    position: absolute;
    left: 0;
    top: 273px;
    width: 1130px;
    height: 654px;
    overflow: hidden;
    background: linear-gradient(180deg, #DDF0FA 0%, var(--foam-blue) 55%, #D6EDF8 100%);
  }
  .headline {
    position: absolute;
    right: 22px;
    top: 14px;
    margin: 0;
    font-weight: 700;
    font-size: 74px;
    line-height: 1;
    letter-spacing: -1px;
    color: var(--brand-blue);
    white-space: nowrap;
  }
  .company {
    position: absolute;
    right: 22px;
    top: 102px;
    margin: 0;
    font-weight: 700;
    font-size: 54px;
    line-height: 1;
    color: var(--ocean-blue);
    white-space: nowrap;
  }
  .brand-mark {
    position: absolute;
    left: 30px;
    top: 110px;
    width: 230px;
    height: 330px;
    display: flex;
    flex-direction: column;
    align-items: center;
    justify-content: center;
    gap: 18px;
  }
  .brand-mark .dot {
    width: 160px;
    height: 160px;
    border-radius: 50%;
    background: var(--sky-blue);
  }
  .brand-mark .name {
    font-weight: 700;
    font-size: 26px;
    color: var(--navy);
    white-space: nowrap;
  }
  .hero-photo {
    position: absolute;
    left: 265px;
    top: 186px;
    width: 325px;
    height: 255px;
    border-radius: 160px 160px 0 0;
    background: radial-gradient(ellipse at 50% 40%, #E9BC98 0%, #DDA47C 45%, #CFE6F3 85%);
  }
  .services {
    position: absolute;
    left: 622px;
    top: 200px;
    margin: 0;
    padding: 0;
    list-style: none;
  }
  .services li {
    display: flex;
    align-items: center;
    gap: 16px;
    height: 54px;
    font-weight: 600;
    font-size: 40px;
    color: var(--navy);
    white-space: nowrap;
  }
  .services svg {
    width: 30px;
    height: 30px;
    flex: none;
  }
  .contact-band {
    position: absolute;
    left: 0;
    top: 383px;
    width: 1130px;
    height: 271px;
  }
  .address {
    position: absolute;
    right: 26px;
    top: 396px;
    margin: 0;
    font-weight: 500;
    font-size: 26px;
    color: var(--white);
    white-space: nowrap;
  }
  .phone {
    position: absolute;
    right: 26px;
    top: 446px;
    margin: 0;
    font-weight: 700;
    font-size: 80px;
    line-height: 1.1;
    color: var(--white);
    white-space: nowrap;
  }
  .email {
    position: absolute;
    left: 38px;
    top: 506px;
    margin: 0;
    font-weight: 600;
    font-size: 42px;
    color: var(--navy);
    white-space: nowrap;
  }
</style>
</head>
<body>
<div class="canvas">
  <section class="billboard">
    <div class="brand-mark">
      <div class="dot"></div>
      <span class="name">RUSTY'S POOLS</span>
    </div>

    <div class="hero-photo" role="img" aria-label="Photo of a smiling young girl in sunglasses leaning on the edge of a swimming pool"></div>

    <svg class="contact-band" viewBox="0 0 1130 271" preserveAspectRatio="none" aria-hidden="true">
      <rect x="0" y="58" width="563" height="213" fill="var(--white)"/>
      <polygon points="563,0 1130,0 1130,271 518,271" fill="var(--navy)"/>
    </svg>

    <h1 class="headline">RUSTY &amp; CALDER PEMBROOK</h1>
    <h2 class="company">RUSTY'S POOLS &amp; SERVICE</h2>

    <ul class="services">
      <li><svg viewBox="0 0 30 30" aria-hidden="true"><polygon points="2,2 28,15 2,28 9,15" fill="var(--navy)"/></svg>Repairs</li>
      <li><svg viewBox="0 0 30 30" aria-hidden="true"><polygon points="2,2 28,15 2,28 9,15" fill="var(--navy)"/></svg>New Construction</li>
      <li><svg viewBox="0 0 30 30" aria-hidden="true"><polygon points="2,2 28,15 2,28 9,15" fill="var(--navy)"/></svg>Weekly maintenance</li>
    </ul>

    <p class="address">2750 marlow Rd brenton, Ga 31590</p>
    <p class="phone">912•555•0147</p>
    <p class="email">rusty@rppools.com</p>
  </section>
</div>
</body>
</html>
```